Dyslexia Assessment Business card design

we need a business card design for a new company based in New Hampshire called Maple Path Learning of NH. We provide dyslexia assessment and consultation
Updates

Can you please add my degrees/certifications Carla Whitmore MA, MEd NH Certified Specialist in the Assessment of Intellectual Functioning Reading and Writing Specialist Learning Disabilities Specialist

I am interested in also creating a web page. If you have experience with webpages that may be useful. I have the domains but am waiting the name of the business to be cleared by the state. I expect this to take place within the month.

I think listing all the certifications is too much. Please just add Carla Whitmore MA, MEd, SAIF

Target Market(s)

parents of kids with dyslexia

Industry/Entity Type

Business

Contact Information for Business Card

Maple Path Learning of NH
Carla Whitmore - Dyslexia Diagnostician/Consultant
42 Tilbury Lane Londonderry, NH 03071
Phone (603)284-7105
WWW.MaplePathLearningofNH-example.com
MaplePathLearningofNH@mailbox-example.com

Requirements
Nice to have
• can have 2 sides not essential though

maybe "dyslexia" in the background spelled wrong or letters backward

```html
<!DOCTYPE html>
<html lang="en">
<head>
<meta charset="utf-8">
<title>Maple Path Learning of NH – Business Card</title>
<link rel="stylesheet" href="https://fonts.googleapis.com/css2?family=Open+Sans:wght@400;600&display=swap">
<style>
  :root {
    --page-bg: #e9e7e3;
    --card-white: #ffffff;
    --card-shade: #eceef0;
    --band-black: #0b0c0e;
    --band-grey: #23262b;
    --accent-light: #5aa6e0;
    --accent-mid: #3b6fd0;
    --accent-violet: #3c33a8;
    --ink-dark: #3a3d42;
    --ink-light: #e9ecef;
    --icon-fill: #4e8fc9;
  }
  html, body {
    margin: 0;
    padding: 0;
    width: 1200px;
    height: 1023px;
    overflow: hidden;
    background: var(--page-bg);
    font-family: "Open Sans", Arial, sans-serif;
  }
  .business-card {
    position: absolute;
    left: 75px;
    top: 211px;
    width: 1050px;
    height: 600px;
    background: linear-gradient(160deg, var(--card-white) 40%, var(--card-shade));
    box-shadow: 0 12px 30px rgba(0,0,0,0.25);
    overflow: hidden;
  }
  .card-art {
    position: absolute;
    inset: 0;
  }
  .brand {
    position: absolute;
    left: 80px;
    top: 92px;
    display: flex;
    align-items: center;
    gap: 16px;
  }
  .brand-dot {
    width: 30px;
    height: 30px;
    border-radius: 50%;
    background: var(--accent-mid);
  }
  .brand-name {
    font-size: 44px;
    font-weight: 400;
    line-height: 1.2;
    color: var(--ink-dark);
    letter-spacing: -0.5px;
    white-space: nowrap;
  }
  .person {
    position: absolute;
    left: 70px;
    top: 408px;
    color: var(--ink-light);
  }
  .person-name {
    margin: 0;
    font-size: 30px;
    font-weight: 600;
    color: var(--accent-light);
    letter-spacing: 0.3px;
  }
  .person-role {
    margin: 2px 0 14px;
    font-size: 20px;
    font-weight: 400;
  }
  .contact-list {
    list-style: none;
    margin: 0;
    padding: 0;
    font-size: 19px;
    line-height: 31px;
  }
  .contact-list li {
    display: flex;
    align-items: center;
    gap: 10px;
  }
  .contact-icon {
    width: 20px;
    height: 20px;
    flex: none;
  }
  .address {
    position: absolute;
    left: 720px;
    top: 330px;
    margin: 0;
    font-size: 21px;
    line-height: 31px;
    color: var(--ink-light);
    font-style: normal;
  }
</style>
</head>
<body>
  <div class="business-card">
    <svg class="card-art" width="1050" height="600" viewBox="0 0 1050 600" aria-hidden="true">
      <defs>
        <linearGradient id="accentStripe" x1="0" y1="0" x2="1" y2="0">
          <stop offset="0" stop-color="#7cc0ee"/>
          <stop offset="0.45" stop-color="#3b6fd0"/>
          <stop offset="1" stop-color="#3c33a8"/>
        </linearGradient>
        <linearGradient id="bandFill" x1="0" y1="0" x2="1" y2="1">
          <stop offset="0" stop-color="#23262b"/>
          <stop offset="0.5" stop-color="#0b0c0e"/>
          <stop offset="1" stop-color="#15171a"/>
        </linearGradient>
      </defs>
      <path class="accent-stripe" d="M0,360 C400,346 790,170 1050,-20 L1050,600 L0,600 Z" fill="url(#accentStripe)"/>
      <path class="dark-band" d="M0,384 C420,374 810,230 1050,48 L1050,600 L0,600 Z" fill="url(#bandFill)"/>
    </svg>

    <div class="brand">
      <span class="brand-dot"></span>
      <span class="brand-name">Maple Path Learning of NH</span>
    </div>

    <div class="person">
      <h1 class="person-name">CARLA WHITMORE MA, MEd, SAIF</h1>
      <p class="person-role">Dyslexia Diagnostician | Consultant</p>
      <ul class="contact-list">
        <li>
          <svg class="contact-icon" viewBox="0 0 20 20" aria-hidden="true">
            <circle cx="10" cy="10" r="10" fill="var(--icon-fill)"/>
            <path d="M6.5 5.5 L8.5 5.5 L9.3 8 L8 9 C8.7 10.6 9.6 11.5 11 12.1 L12 10.8 L14.5 11.6 L14.5 13.6 C10 14 6 10 6.5 5.5 Z" fill="#0b0c0e"/>
          </svg>
          (603)284-7105
        </li>
        <li>
          <svg class="contact-icon" viewBox="0 0 20 20" aria-hidden="true">
            <circle cx="10" cy="10" r="10" fill="var(--icon-fill)"/>
            <rect x="5" y="6.5" width="10" height="7" fill="none" stroke="#0b0c0e" stroke-width="1.4"/>
            <path d="M5 6.5 L10 10.5 L15 6.5" fill="none" stroke="#0b0c0e" stroke-width="1.4"/>
          </svg>
          MaplePathLearningofNH@mailbox-example.com
        </li>
        <li>
          <svg class="contact-icon" viewBox="0 0 20 20" aria-hidden="true">
            <circle cx="10" cy="10" r="10" fill="var(--icon-fill)"/>
            <circle cx="10" cy="10" r="5.5" fill="none" stroke="#0b0c0e" stroke-width="1.3"/>
            <ellipse cx="10" cy="10" rx="2.3" ry="5.5" fill="none" stroke="#0b0c0e" stroke-width="1.1"/>
            <path d="M4.5 10 H15.5" stroke="#0b0c0e" stroke-width="1.1"/>
          </svg>
          WWW.MaplePathLearningofNH-example.com
        </li>
      </ul>
    </div>

    <address class="address">42 Tilbury Lane Londonderry<br>NH 03071</address>
  </div>
</body>
</html>
```